Design Carton For Perfume

Hello,

Please design JUST THE CARTON for this perfume.

The perfume is Named

Brent Vayle
Danica Thorn

Please design it close to the same appearance as the bottle. Using same colors and look.

Thank you!

```html
<!DOCTYPE html>
<html lang="en">
<head>
<meta charset="utf-8">
<title>Brent Vayle – Danica Thorn Carton</title>
<link rel="stylesheet" href="https://fonts.googleapis.com/css2?family=Pinyon+Script&family=Libre+Caslon+Text&family=Source+Sans+3:wght@400&display=swap">
<style>
  :root {
    --paper: #ffffff;
    --outline: #231f20;
    --ink-script: #2e2a26;
    --pink: #eab3bf;
    --pink-deep: #c0737e;
    --pink-soft: #f6dde3;
    --lavender: #d7b9df;
    --steel: #bcbec0;
    --frame-grey: #b5b5b5;
    --label-grey: #939598;
  }
  * { margin: 0; padding: 0; box-sizing: border-box; }
  html, body {
    width: 1200px; height: 1200px; overflow: hidden;
    background: var(--paper);
  }
  .canvas { position: relative; width: 1200px; height: 1200px; }
  .carton-front {
    position: absolute; left: 195px; top: 124px; width: 819px; height: 819px;
    border: 1px solid var(--outline); background: var(--paper); overflow: hidden;
  }
  .bottle-art { position: absolute; left: 0; top: 0; }
  .brand-title {
    position: absolute; left: 0; right: 0; top: 60px; text-align: center;
    font-family: "Pinyon Script", cursive; font-size: 118px; line-height: 1;
    color: var(--ink-script); white-space: nowrap;
  }
  .band-name {
    position: absolute; top: 352px; width: 210px; text-align: center;
    font-family: "Pinyon Script", cursive; font-size: 38px; line-height: 1;
    color: var(--paper); white-space: nowrap;
  }
  .band-name.left { left: 150px; }
  .band-name.right { left: 453px; }
  .medallion-name {
    position: absolute; left: 344px; top: 600px; width: 130px; text-align: center;
    font-family: "Libre Caslon Text", serif; font-size: 27px; line-height: 1.08;
    color: var(--paper); text-shadow: 1px 1px 2px rgba(80,40,45,0.6);
  }
  .carton-hinge {
    position: absolute; left: 211px; top: 944px; width: 787px; height: 46px;
    background: var(--steel); border: 1px solid var(--outline);
  }
  .carton-base {
    position: absolute; left: 195px; top: 991px; width: 819px; height: 157px;
    border: 1px solid var(--outline); background: var(--paper);
    text-align: center; font-family: "Source Sans 3", sans-serif; color: var(--label-grey);
  }
  .product-type { margin-top: 44px; font-size: 29px; line-height: 1; letter-spacing: 0.3px; }
  .product-volume { margin-top: 12px; font-size: 27px; line-height: 1; word-spacing: 3px; }
</style>
</head>
<body>
<div class="canvas">
  <section class="carton-front">
    <svg class="bottle-art" width="819" height="819" viewBox="0 0 819 819">
      <defs>
        <linearGradient id="bottleTone" x1="0.3" y1="0" x2="0.6" y2="1">
          <stop offset="0" stop-color="#e9aab8"/>
          <stop offset="0.45" stop-color="#f3d3dd"/>
          <stop offset="1" stop-color="#d9c0e4"/>
        </linearGradient>
        <linearGradient id="bandLeft" x1="0" x2="1">
          <stop offset="0" stop-color="#efb9c4"/>
          <stop offset="1" stop-color="#ffffff"/>
        </linearGradient>
        <linearGradient id="bandRight" x1="1" x2="0">
          <stop offset="0" stop-color="#efb9c4"/>
          <stop offset="1" stop-color="#ffffff"/>
        </linearGradient>
      </defs>
      <g role="img" aria-label="Illustration of a ribbed glass perfume bottle with a pink round stopper, pink bow and silver chains, over soft pink and lavender brush strokes">
        <rect x="140" y="24" width="536" height="784" rx="70" fill="url(#bottleTone)" opacity="0.55"/>
      </g>
      <rect class="band-left" x="2" y="338" width="130" height="71" fill="url(#bandLeft)"/>
      <rect class="band-right" x="687" y="338" width="130" height="71" fill="url(#bandRight)"/>
      <rect class="bottle-label" x="142" y="336" width="536" height="75" rx="14"
            fill="#f6dde3" stroke="#b5b5b5" stroke-width="3"/>
      <circle class="medallion" cx="409" cy="645" r="70" fill="#eeb8c3" stroke="#c0737e" stroke-width="6"/>
    </svg>
    <div class="brand-title">Brent Vayle</div>
    <div class="band-name left">Brent Vayle</div>
    <div class="band-name right">Brent Vayle</div>
    <div class="medallion-name">Danica<br>Thorn</div>
  </section>
  <div class="carton-hinge"></div>
  <section class="carton-base">
    <p class="product-type">EAU DE PARFUM</p>
    <p class="product-volume">e100ml&nbsp;&nbsp; 3.4 fl. oz.</p>
  </section>
</div>
</body>
</html>
```